Would need to a simple sticker for baby wipe. (Layout provided)

Hi guys,
I would need to design a removable sticker that located under the lid of baby wipe, please look at picture 1 then you will get what it is (the yellow oval). It just a sticker that consumer will removed at the beginning in order to take out the wipe.
-Picture 2 and 3: are some ideas from other competitors. As you could see, most are oval shapes, and the ideas are quite variety, some are very simple, some is more complicate.
-Picture 4: is my actual product.
-File "layout.AI" is where you could begin with (or not, if you want). I hope you could help to design a simple design, but still somehow match with the overall design of the product (which already have quite soft and colorful pastel).
Dimension is around 6x3 cm
The idea are totally freedom.
Thank you for your help

```html
<!DOCTYPE html>
<html lang="en">
<head>
<meta charset="utf-8">
<title>Baby Wipe Lid Sticker – Two Colourways</title>
<link href="https://fonts.googleapis.com/css2?family=Black+Ops+One&family=Montserrat:wght@700&display=swap" rel="stylesheet">
<style>
  :root {
    --page: #ffffff;
    --sky: #429fb5;
    --sand: #c5bdac;
    --white: #fbfdfd;
    --ink: #333b40;
  }
  html, body {
    margin: 0;
    padding: 0;
    overflow: hidden;
    background: var(--page);
  }
  .canvas {
    width: 849px;
    height: 1200px;
    display: block;
  }
  .sticker-sky .body { fill: var(--sky); }
  .sticker-sand .body { fill: var(--sand); }
  .pull-disc { fill: var(--white); }
  .stitch {
    fill: none;
    stroke: var(--white);
    stroke-width: 2.6;
    stroke-dasharray: 14 9;
  }
  .tagline {
    font-family: "Black Ops One", "Arial Black", sans-serif;
    font-size: 66px;
    fill: var(--white);
    text-anchor: middle;
  }
  .open-label {
    font-family: "Montserrat", Arial, sans-serif;
    font-weight: 700;
    font-size: 11px;
    letter-spacing: 0.5px;
    fill: var(--ink);
    text-anchor: middle;
  }
  .turn-arrow {
    fill: none;
    stroke: var(--sky);
    stroke-width: 9;
  }
  .sticker-sand .turn-arrow { stroke: var(--sand); }
  .sticker-sky .arrow-head { fill: var(--sky); }
  .sticker-sand .arrow-head { fill: var(--sand); }
</style>
</head>
<body>
<svg class="canvas" viewBox="0 0 849 1200" xmlns="http://www.w3.org/2000/svg">
  <defs>
    <mask id="tab-gap-right">
      <rect width="849" height="1200" fill="#fff"/>
      <circle cx="734" cy="324" r="67" fill="#000"/>
    </mask>
    <mask id="tab-gap-left">
      <rect width="849" height="1200" fill="#fff"/>
      <circle cx="98" cy="814" r="67" fill="#000"/>
    </mask>
  </defs>

  <!-- Sky colourway, pull tab on the right -->
  <g class="sticker-sky">
    <g role="img" aria-label="Sticker body with faint all-over pattern of baby items: bottles, pacifiers, rattles, blocks and toys">
      <rect class="body" x="20.5" y="125.8" width="729" height="397" rx="164"/>
      <circle class="body" cx="734" cy="324" r="81"/>
    </g>
    <rect class="stitch" x="48" y="153" width="668" height="342" rx="138" mask="url(#tab-gap-right)"/>
    <path class="stitch" d="M 716 265 A 67 67 0 0 0 716 383"/>
    <circle class="pull-disc" cx="734" cy="324" r="56"/>
    <path class="turn-arrow" d="M 753 290 A 36 36 0 0 1 768 345"/>
    <path class="arrow-head" d="M 752 335 L 768 357 L 778 342 L 770 338 L 764 318 Z"/>
    <text class="open-label" transform="translate(741 324) rotate(90)" dy="4">OPEN</text>
    <text class="tagline" x="381" y="316">TAGLINE</text>
    <text class="tagline" x="381" y="381">GOES HERE</text>
  </g>

  <!-- Sand colourway, pull tab on the left -->
  <g class="sticker-sand">
    <g role="img" aria-label="Sticker body with faint all-over pattern of baby items: bottles, pacifiers, rattles, blocks and toys">
      <rect class="body" x="92" y="615.5" width="721" height="397" rx="164"/>
      <circle class="body" cx="98" cy="814" r="81"/>
    </g>
    <rect class="stitch" x="120" y="643" width="665" height="342" rx="138" mask="url(#tab-gap-left)"/>
    <path class="stitch" d="M 120 755 A 67 67 0 0 1 120 873"/>
    <circle class="pull-disc" cx="98" cy="814" r="56"/>
    <path class="turn-arrow" d="M 80 785 A 36 36 0 0 0 68 840"/>
    <path class="arrow-head" d="M 62 840 L 66 858 L 88 842 L 76 824 L 72 838 Z"/>
    <text class="open-label" transform="translate(104 814) rotate(90)" dy="4">OPEN</text>
    <text class="tagline" x="455" y="806">TAGLINE</text>
    <text class="tagline" x="455" y="871">GOES HERE</text>
  </g>
</svg>
</body>
</html>
```